Business Cards

I'd like help creating business cards with the full logo "Veltrona Capital Partners" on the back of the card (navy background with white writing), and abbreviated logo "VCP" on the front. Would like to list name, title, phone number, email, and website listed on front of card. Would like to keep very simple. Front font Arial or similar.

```html
<!DOCTYPE html>
<html lang="en">
<head>
<meta charset="utf-8">
<title>Veltrona Capital Partners – Business Cards</title>
<link rel="stylesheet" href="https://fonts.googleapis.com/css2?family=Lato:wght@400;700;900&display=swap">
<style>
  :root {
    --navy: #1f3a6e;
    --navy-deep: #1b3261;
    --white: #ffffff;
    --grey: #8a8f98;
    --backdrop: #e9eaec;
  }
  * { box-sizing: border-box; margin: 0; padding: 0; }
  html, body { width: 1200px; height: 952px; overflow: hidden; }
  body {
    background: var(--backdrop);
    font-family: "Lato", Arial, sans-serif;
    display: flex;
    align-items: center;
    justify-content: center;
    gap: 40px;
  }
  .card {
    width: 520px;
    height: 297px;
    border-radius: 22px;
    position: relative;
    overflow: hidden;
    box-shadow: 0 6px 18px rgba(0,0,0,0.12);
  }

  /* Front */
  .card-front { background: var(--white); }
  .front-mark {
    position: absolute;
    top: 34px;
    left: 235px;
    font-size: 64px;
    font-weight: 900;
    color: var(--navy);
    letter-spacing: 2px;
    line-height: 1;
  }
  .holder {
    position: absolute;
    top: 140px;
    left: 40px;
  }
  .holder-name {
    font-size: 20px;
    color: var(--navy);
    letter-spacing: 0.5px;
    font-weight: 400;
    white-space: nowrap;
  }
  .holder-name strong { font-weight: 900; }
  .holder-title {
    margin-top: 4px;
    font-size: 15px;
    color: var(--grey);
    text-align: right;
  }
  .contacts {
    position: absolute;
    top: 168px;
    left: 262px;
    list-style: none;
  }
  .contacts li {
    display: flex;
    align-items: center;
    gap: 9px;
    font-size: 14px;
    color: var(--grey);
    height: 22px;
  }
  .contact-icon {
    width: 17px;
    height: 17px;
    background: var(--navy);
    border-radius: 3px;
    display: flex;
    align-items: center;
    justify-content: center;
    flex: none;
  }
  .address-band {
    position: absolute;
    left: 0;
    right: 0;
    bottom: 14px;
    height: 30px;
    background: var(--navy);
    color: var(--white);
    font-size: 15px;
    letter-spacing: 0.3px;
    display: flex;
    align-items: center;
    padding-left: 40px;
  }

  /* Back */
  .card-back {
    background: var(--navy-deep);
    display: flex;
    align-items: center;
    justify-content: center;
  }
  .back-mark {
    color: var(--white);
    font-weight: 900;
    text-align: center;
    line-height: 1;
  }
  .back-mark-name {
    font-size: 52px;
    letter-spacing: 2px;
  }
  .back-mark-sub {
    margin-top: 10px;
    font-size: 17px;
    letter-spacing: 6px;
  }
</style>
</head>
<body>
  <section class="card card-front" aria-label="Business card front">
    <div class="front-mark">VCP</div>
    <div class="holder">
      <p class="holder-name">DANIEL R. <strong>WHITFORD</strong></p>
      <p class="holder-title">Managing Director</p>
    </div>
    <ul class="contacts">
      <li>
        <span class="contact-icon">
          <svg width="11" height="11" viewBox="0 0 24 24"><path fill="#fff" d="M6.6 10.8a15.1 15.1 0 0 0 6.6 6.6l2.2-2.2c.3-.3.7-.4 1-.2 1.1.4 2.3.6 3.6.6.6 0 1 .4 1 1V20c0 .6-.4 1-1 1A17 17 0 0 1 3 4c0-.6.4-1 1-1h3.5c.6 0 1 .4 1 1 0 1.3.2 2.5.6 3.6.1.3 0 .7-.2 1z"/></svg>
        </span>+00 987 654 32
      </li>
      <li>
        <span class="contact-icon">
          <svg width="11" height="11" viewBox="0 0 24 24"><rect x="2" y="5" width="20" height="14" rx="1" fill="#fff"/><path d="M2 6l10 7 10-7" stroke="#1f3a6e" stroke-width="2" fill="none"/></svg>
        </span>hello@veltronacap.com
      </li>
      <li>
        <span class="contact-icon">
          <svg width="11" height="11" viewBox="0 0 24 24"><path fill="#fff" d="M5 3l14 7-6 2-2 6z"/></svg>
        </span>www.veltronacap.com
      </li>
    </ul>
    <div class="address-band">2170 Harbor Ridge Avenue Arlington, VA 22201</div>
  </section>

  <section class="card card-back" aria-label="Business card back">
    <div class="back-mark">
      <p class="back-mark-name">VELTRONA</p>
      <p class="back-mark-sub">CAPITAL PARTNERS</p>
    </div>
  </section>
</body>
</html>
```